KOV Business Card

the business card should be double sided.
Will need to be Korean on one side and english on the other.
it will need to have:

address
website
skype
phone
cell
fax
name
title
email

just put in dummy details to start - i will then give you correct info once we have the format right.

Also - if you feel creative about the logo we are happy to make some amendments to it so it looks right. We are still at early stages with the logo so happy if you have suggestions around the logo concept.
Updates

The deadline for this has been brought forward to Wednesday 11th December. We can not review any designs after this date.

we will need to make a decision by Wednesday 11th December, so please have designs in by this date and not by the deadline set by craftfolio

Target Market(s)

large companies, executives

Industry/Entity Type

Business

Colors

Designer to choose colors to be used in the design.

Requirements
Must have
• double sided - english on one side and korean on the other. we will give you korean wording once we have a design we like.

```html
<!DOCTYPE html>
<html lang="en">
<head>
<meta charset="utf-8">
<title>KOV Business Card</title>
<link rel="stylesheet" href="https://fonts.googleapis.com/css2?family=Crimson+Text:wght@400;600&family=Fira+Sans:wght@400;500;600&display=swap">
<style>
  :root {
    --backdrop: #c9c9c9;
    --card: #ffffff;
    --brand-blue: #0b448f;
    --ink: #2a2a2a;
    --ink-soft: #3c3c3c;
  }
  * { box-sizing: border-box; margin: 0; padding: 0; }
  html, body {
    width: 1200px;
    height: 835px;
    overflow: hidden;
    background: var(--backdrop);
  }
  .business-card {
    position: absolute;
    left: 100px;
    top: 132px;
    width: 1000px;
    height: 571px;
    background: var(--card);
    box-shadow: 0 6px 24px rgba(0,0,0,0.12);
  }
  .identity {
    position: absolute;
    left: 62px;
    top: 46px;
  }
  .identity__name {
    font-family: "Crimson Text", Georgia, serif;
    font-weight: 600;
    font-size: 46px;
    line-height: 1;
    color: var(--brand-blue);
  }
  .identity__title {
    margin-top: 4px;
    font-family: "Fira Sans", Arial, sans-serif;
    font-weight: 500;
    font-size: 14px;
    letter-spacing: 3.5px;
    color: var(--ink-soft);
  }
  .rule {
    position: absolute;
    left: 62px;
    width: 30px;
    height: 4px;
    background: var(--brand-blue);
  }
  .rule--top { top: 198px; }
  .rule--bottom { top: 392px; }
  .contact-list {
    position: absolute;
    left: 62px;
    top: 212px;
    list-style: none;
    font-family: "Fira Sans", Arial, sans-serif;
    font-size: 19px;
    line-height: 29px;
    color: var(--ink);
  }
  .contact-list__label { font-weight: 600; }
  .address {
    position: absolute;
    left: 62px;
    top: 425px;
    font-family: "Crimson Text", Georgia, serif;
    font-size: 21px;
    color: var(--ink);
  }
  .brand-column {
    position: absolute;
    left: 830px;
    top: 0;
    width: 95px;
    height: 571px;
  }
  .brand-column__cap {
    position: absolute;
    left: 0; top: 0;
    width: 95px;
    height: 38px;
    background: var(--brand-blue);
  }
  .brand-column__band {
    position: absolute;
    left: 0; top: 262px;
    width: 95px;
    height: 309px;
    background: var(--brand-blue);
  }
  .brand-mark {
    position: absolute;
    left: -20px;
    top: 150px;
    width: 135px;
    text-align: center;
    font-family: "Fira Sans", Arial, sans-serif;
    font-weight: 500;
    font-size: 48px;
    letter-spacing: 1px;
    color: var(--brand-blue);
  }
</style>
</head>
<body>
  <article class="business-card">
    <header class="identity">
      <h1 class="identity__name">Full Name</h1>
      <p class="identity__title">DIRECTOR</p>
    </header>

    <div class="rule rule--top"></div>
    <ul class="contact-list">
      <li><span class="contact-list__label">phone:</span> 123.456.7890</li>
      <li><span class="contact-list__label">cell:</span> 704.555.0182</li>
      <li><span class="contact-list__label">fax:</span> 123.456.7890</li>
      <li><span class="contact-list__label">skype:</span> kovname</li>
      <li><span class="contact-list__label">email:</span> kov@kov.com</li>
      <li><span class="contact-list__label">website:</span> kvm.com</li>
    </ul>
    <div class="rule rule--bottom"></div>
    <p class="address">4215 Road Name, Suite 610, Halden, MA 14170</p>

    <aside class="brand-column">
      <div class="brand-column__cap"></div>
      <p class="brand-mark">KOV</p>
      <div class="brand-column__band"></div>
    </aside>
  </article>
</body>
</html>
```